MOREVI VEGAN SUSHI

www.morevi-restaurant.de
We are open in 2018 and are an innovative restaurant from Munich. We would like a cool design for our drinks and food menu. It's very simple at the moment. See the File menu. In any case, our logo should appear. On the website we use neutraface as a font. But it's not a must. We are only open in the evening and appeal to a young, upscale audience.

```html
<!DOCTYPE html>
<html lang="de">
<head>
<meta charset="utf-8">
<title>Morevi Vegan Sushi – Speisekarte</title>
<link href="https://fonts.googleapis.com/css2?family=Questrial&display=swap" rel="stylesheet">
<style>
  :root{
    --bg:#2a2a2b;
    --ink:#0d0d0d;
    --paper:#ecebe8;
    --paper-dark:#dedcd8;
    --red:#e3202a;
    --text-dark:#1b1b1b;
    --text-light:#f4f4f4;
    --green:#6aa84f;
  }
  *{box-sizing:border-box;margin:0;padding:0}
  html,body{width:1200px;height:800px;overflow:hidden}
  body{background:var(--bg);font-family:"Questrial",sans-serif;position:relative}
  .page{position:absolute;top:30px;width:572px;height:740px;display:flex;flex-direction:column;overflow:hidden}
  .page--food{left:18px}
  .page--menu{left:610px}
  .paper{background:radial-gradient(circle at 30% 40%,var(--paper),var(--paper-dark));color:var(--text-dark)}
  .ink{background:var(--ink);color:var(--text-light)}
  .rule{background:var(--red)}
  .title{color:var(--red);font-size:17px;line-height:1.2;font-weight:400}
  .price{color:var(--red)}
  .big-price{color:var(--red);font-size:17px;line-height:1.2}
  .photo{position:absolute}
  .photo--framed{border:5px solid var(--red)}

  /* left page */
  .hero{position:relative;height:200px}
  .brand{position:absolute;left:0;right:0;top:58px;text-align:center}
  .brand__mark{display:block;width:46px;height:46px;border-radius:50%;background:var(--ink);margin:0 auto 16px}
  .brand__name{font-size:15px;letter-spacing:10px;color:var(--text-dark);padding-left:10px}
  .photo--ramen{left:65px;top:93px;width:121px;height:121px;background:radial-gradient(circle,#b8693a,#6e4a2a 60%,#ddd 62%,#8a6a4a)}
  .photo--nigiri{left:386px;top:93px;width:121px;height:121px;background:radial-gradient(circle at 55% 45%,#d8342c,#8e1a16 45%,#111 70%)}
  .feature{height:168px;position:relative;font-size:11px;line-height:19px;text-align:center}
  .feature__col{position:absolute;top:40px;width:300px}
  .feature__col--chef{left:14px;top:40px}
  .feature__col--omakase{left:287px;top:32px}
  .vdash{position:absolute;border-left:2px dashed var(--red)}
  .sets{height:243px;position:relative;font-size:11px;line-height:18.5px;text-align:center}
  .set{position:absolute;top:32px;width:190px}
  .set--1{left:1px}.set--2{left:185px}.set--3{left:376px}
  .set .title{margin-bottom:2px}
  .band-rule{height:4px}
  .footer-photo{height:125px;position:relative;background:linear-gradient(100deg,#2b2420,#d9b39a 30%,#eee2d4 45%,#e98a5e 60%,#3a3230 85%)}
  .web{position:absolute;left:14px;bottom:12px;color:var(--red);font-size:13px}

  /* right page */
  .starters{height:170px;display:flex}
  .photo--miso{position:static;width:200px;background:radial-gradient(circle at 50% 55%,#6b7a3a,#3a2e18 45%,#111 62%,#6d7a80)}
  .photo--edamame{position:static;width:158px;background:radial-gradient(circle,#5fa040,#2e5520 40%,#8e2020 60%,#3a3f48)}
  .starters__list{flex:1;text-align:center;font-size:11px;line-height:22px;padding-top:28px}
  .starters__list .title{margin-bottom:2px}
  .thick-rule{height:9px}
  .split{height:185px;position:relative;font-size:11px;line-height:19px}
  .split__col{position:absolute;top:26px}
  .split__col--sushi{left:44px}
  .split__col--small{left:328px}
  .split__col .title{margin-bottom:1px}
  .mains{height:183px;text-align:center;font-size:11px;line-height:17.7px;padding-top:10px}
  .mains .title{margin-bottom:2px}
  .desserts{height:125px;display:flex}
  .photo--sorbet{position:static;width:125px;background:radial-gradient(circle at 45% 55%,#a0182a,#e8e4e4 55%,#c9c5c6)}
  .photo--cheesecake{position:static;width:125px;background:linear-gradient(160deg,#3a2a20,#c8a070 40%,#f2e6c8 60%,#5a4a40)}
  .desserts__list{flex:1;text-align:center;font-size:11px;line-height:17.6px;padding-top:14px}
  .desserts__list .title{font-size:12px}
  .vegan{color:var(--green);font-size:18px;line-height:22px}
  .notice{height:59px;text-align:center;font-size:13px;line-height:16px;padding-top:12px}
</style>
</head>
<body>

<section class="page page--food">
  <header class="hero paper">
    <div class="brand">
      <span class="brand__mark"></span>
      <span class="brand__name">MOREVI</span>
    </div>
    <div class="photo photo--framed photo--ramen" role="img" aria-label="Schale Ramen mit Gemüse und Nudeln"></div>
    <div class="photo photo--framed photo--nigiri" role="img" aria-label="Nigiri auf schwarzem Grund"></div>
  </header>

  <div class="feature ink">
    <div class="feature__col feature__col--chef">
      <h2 class="title">CHEF MENÜ mit Aperitiv</h2>
      <p>für 2 Personen</p>
      <p>Kleine Portion RAMENSUPPE mit Gemüse &amp; Nudeln</p>
      <p>MINI SET</p>
      <p>DESSERT</p>
      <p class="big-price">81,00€</p>
    </div>
    <div class="vdash" style="left:314px;top:10px;height:150px"></div>
    <div class="feature__col feature__col--omakase">
      <h2 class="title">OMAKASE</h2>
      <p>für 2 Personen</p>
      <p>EDAMAME</p>
      <p>OMAKASE SET mit 8 Spezialitäten des<br>Hauses</p>
      <p>PANA COTTA mit Beeren</p>
      <p class="big-price">68,00€</p>
    </div>
  </div>

  <div class="sets paper">
    <div class="set set--1">
      <h3 class="title">SET 1</h3>
      <p>HOSOMAKI</p><p>FUTOMAKI</p><p>NIGIRI</p><p>KÜRBISKROKETTEN</p>
      <p>WAKAME GURKEN SALAT</p><p>PICKLES</p><p>GYOZA TEIGTASCHEN</p><p>SUSHI CAKE</p>
      <p class="big-price">33,90€</p>
    </div>
    <div class="vdash" style="left:186px;top:38px;height:210px"></div>
    <div class="set set--2">
      <h3 class="title">SET 2</h3>
      <p>HOSOMAKI</p><p>FUTOMAKI</p><p>PICKLES</p><p>SUSHI “THUNA” CAKE</p>
      <p>Crispy AUBERGINEN mit Mayo</p><p>AUBERGINE DENGAKU</p>
      <p class="big-price">31,90€</p>
    </div>
    <div class="vdash" style="left:373px;top:38px;height:210px"></div>
    <div class="set set--3">
      <h3 class="title">SET 3</h3>
      <p>HOSOMAKI</p><p>URAMAKI</p><p>NIGIRI</p><p>GEMÜSE TEMPURA</p>
      <p>Crispy TOFUSTICKS mit Mayo</p><p>WAKAME SHIRA AE</p>
      <p class="big-price">28,90€</p>
    </div>
  </div>

  <div class="band-rule rule"></div>
  <footer class="footer-photo" role="img" aria-label="Nahaufnahme von Maki-Rollen">
    <span class="web">www.morevi-restaurant.de</span>
  </footer>
</section>

<section class="page page--menu">
  <div class="starters ink">
    <div class="photo photo--miso" role="img" aria-label="Misosuppe mit Tofu in schwarzer Schale"></div>
    <div class="starters__list">
      <h2 class="title">VORSPEISEN</h2>
      <p>MISO SUPPE <span class="price">5,50€</span></p>
      <p>EDAMAME MIT SALZ/CHILI <span class="price">4,50€</span></p>
      <p>SEIDENTOFU in hausgemachter</p>
      <p>Sauce mit Mandeln <span class="price">5,50€</span></p>
    </div>
    <div class="photo photo--edamame" role="img" aria-label="Edamame mit Chili in quadratischer Schale"></div>
  </div>
  <div class="thick-rule rule"></div>

  <div class="split paper">
    <div class="split__col split__col--sushi">
      <h2 class="title">SUSHI</h2>
      <p>URAMAKI mit Tempuragemüse <span class="price">8,90€</span></p>
      <p>FUTOMAKI wechselndes Gemüse <span class="price">8,00€</span></p>
      <p>URAMAKI mit Austernpilze <span class="price">7,50€</span></p>
      <p>HOSOMAKI Gurke Avocado <span class="price">5,50€</span></p>
      <p>HOSOMAKI Gurke Shiitake <span class="price">5,50€</span></p>
      <p>TOMATEN NIGIRI <span class="price">4,50€</span></p>
    </div>
    <div class="vdash" style="left:279px;top:20px;height:152px"></div>
    <div class="split__col split__col--small">
      <h2 class="title">KLEINE GERICHTE</h2>
      <p>GEMÜSE TEMPURA <span class="price">8,00</span></p>
      <p>Crispy TOFUSTICKS mit Mayo <span class="price">8,00€</span></p>
      <p>KÜRBISKROKETTEN mit TANGASHU <span class="price">7,90€</span></p>
      <p>SUSHI “THUNA” CAKE <span class="price">6,90€</span></p>
      <p>SUSHI CAKE CLASSIC <span class="price">6,00€</span></p>
      <p>AUBERGINE DENGAKU <span class="price">5,50€</span></p>
    </div>
  </div>

  <div class="mains ink">
    <h2 class="title">HAUPTSPEISEN</h2>
    <p>Herrlich cremiges KATSU CURRY mit knusprigen Auberginensticks, Reis &amp; Pickles</p>
    <p class="price">17,90€</p>
    <p>RAMEN SUPPE mit Nudeln, Gemüse &amp; Tofu</p>
    <p class="price">14,90€</p>
    <p>CHIRASHI SUSHI BOWL</p>
    <p class="price">13,90€</p>
    <p>SOMMERSALATE mit Sesamdressing &amp; crispy Tofusticks mit Mayo</p>
    <p class="price">12,50€</p>
  </div>
  <div class="thick-rule rule"></div>

  <div class="desserts paper">
    <div class="photo photo--sorbet" role="img" aria-label="Beerensorbet auf weißem Teller"></div>
    <div class="desserts__list">
      <h2 class="title">DESSERT</h2>
      <p>CHEESECAKE mit Beeren <span class="price">6,50€</span></p>
      <p>PANA COTTA mit Beeren <span class="price">5,90€</span></p>
      <p>SORBET des Tages <span class="price">5,50€</span></p>
      <p>SORBET des Tages mit Schuss <span class="price">6,90€</span></p>
      <p class="vegan">All vegan</p>
    </div>
    <div class="photo photo--cheesecake" role="img" aria-label="Stück Cheesecake"></div>
  </div>

  <footer class="notice ink">
    <p>Bitte teilen Sie dem Service unbedingt Allergien mit und fragen Sie nach<br>der Allergiker-Menükarte</p>
  </footer>
</section>

</body>
</html>
```